BriskwayLane.com needs updated website design.

BriskwayLane.com offers individuals a quick, hassle-free way of selling their car, rv, or boat in the Sun City Center, FL area. We will come to the customer's place of choosing in order to give them an in-person offer for their car, rv, or boat. Looking for a website design that will allow users to input their vehicle details as well as their contact info in order to schedule a time and place for our staff to come make them an offer. Currently have an active site that can be referenced.

Target Market(s)

Older people who no longer need their cars.

Industry/Entity Type

Automotive

Coding

Coded - Design and coding required

Number of Pages Required

3 page

Font styles to use
Sans Serif

Colors
a1cd3a
33b8a4

Requirements
Must have
• Trustworthy theme, Emphasis on capturing contact info (contact form visible at all times). Standard privacy policy. Wordpress theme

```html
<!DOCTYPE html>
<html lang="en">
<head>
<meta charset="utf-8">
<title>BriskwayLane.com – Sell Your Car, RV or Boat</title>
<link rel="stylesheet" href="https://fonts.googleapis.com/css2?family=Poppins:wght@400;500;600&family=Yellowtail&display=swap">
<style>
:root{
  --navy:#0f3a6d;
  --navy-deep:#0c3363;
  --green:#a1cd3a;
  --sky:#5cb9d8;
  --ink:#2f3b4a;
  --muted:#5b6470;
  --wood:#ececec;
  --panel:#e8e8e8;
  --white:#ffffff;
  --line:#d2d2d2;
}
*{box-sizing:border-box;margin:0;padding:0}
html,body{width:1200px;height:3224px;overflow:hidden}
body{font-family:"Poppins",sans-serif;color:var(--ink);background:var(--white);position:relative}
.abs{position:absolute}
.btn{position:absolute;display:flex;align-items:center;justify-content:center;border-radius:20px;font-weight:600;font-size:12.5px;color:var(--navy)}
.btn--green{background:var(--green)}
.btn--sky{background:var(--sky)}

/* header */
.site-header{position:absolute;left:0;top:0;width:1200px;height:88px;background:linear-gradient(90deg,#efefef,#f7f7f7 50%,#efefef)}
.call{position:absolute;left:148px;top:34px;font-weight:600;font-size:16px;color:var(--navy);display:flex;align-items:center;gap:6px}
.call .dot{width:18px;height:18px;border-radius:50%;background:var(--green);display:inline-flex;align-items:center;justify-content:center}
.brand{position:absolute;left:0;width:1200px;top:26px;text-align:center;font-weight:600;font-size:21px;color:var(--navy);display:flex;justify-content:center;align-items:center;gap:10px}
.brand .mark{width:22px;height:22px;border-radius:50%;background:var(--sky)}
.main-nav{position:absolute;left:0;top:88px;width:1200px;height:44px;background:var(--navy);display:flex;justify-content:center;align-items:center;gap:30px;font-size:13px;font-weight:500;color:var(--white)}
.main-nav .active{color:var(--sky);position:relative}
.main-nav .active::before{content:"";position:absolute;left:-16px;right:-16px;top:-16px;height:3px;background:var(--green)}
.main-nav .sep{width:4px;height:4px;border-radius:50%;background:var(--white)}

/* hero */
.hero{position:absolute;left:0;top:132px;width:1200px;height:526px;background:linear-gradient(100deg,#2c3238 0%,#4a5056 35%,#8a8a86 60%,#a9a7a2 80%,#7b7c7c 100%)}
.hero h1{position:absolute;left:85px;top:162px;font-size:33px;line-height:42px;font-weight:600;color:var(--white)}
.hero p{position:absolute;left:85px;top:254px;font-size:20px;font-weight:600;color:var(--white)}

/* vehicle chooser */
.chooser{position:absolute;left:0;top:658px;width:1200px;height:327px;background:var(--panel)}
.chooser h2{position:absolute;width:1200px;top:66px;text-align:center;font-size:21px;font-weight:500;color:var(--ink)}
.vehicle{position:absolute;top:131px;width:200px;margin-left:-100px;text-align:center;font-size:14px;color:var(--muted)}
.vehicle .disc{width:88px;height:88px;border-radius:50%;background:var(--white);margin:0 auto 14px;display:flex;align-items:center;justify-content:center}
.vehicle.selected .disc{background:var(--navy);margin-top:8px}
.vehicle.selected{color:var(--navy)}
.divider{position:absolute;top:133px;width:1px;height:131px;background:#cfcfcf}

/* about */
.about-photo{left:85px;top:1071px;width:479px;height:408px;background:linear-gradient(135deg,#d9dde2,#8c9cb5 45%,#2c4d8a 70%,#b9bec4)}
.about-brand{left:656px;top:1118px;font-size:23px;font-weight:600;color:var(--navy);display:flex;align-items:center;gap:12px}
.about-brand .mark{width:26px;height:26px;border-radius:50%;background:var(--sky)}
.about-rule{left:634px;top:1186px;width:457px;height:1px;background:var(--line)}
.about h3{position:absolute;left:634px;top:1214px;width:470px;font-size:22px;line-height:30px;font-weight:400;color:var(--ink)}
.about p{position:absolute;left:634px;top:1296px;width:480px;font-size:13.5px;line-height:23px;color:var(--ink)}

/* promise band */
.promise{position:absolute;left:0;top:1568px;width:1200px;height:360px;background:repeating-linear-gradient(90deg,#ededed 0 58px,#e4e4e4 58px 60px,#f1f1f1 60px 118px,#e6e6e6 118px 120px)}
.promise h2{position:absolute;width:1200px;top:64px;text-align:center;font-size:21.5px;line-height:30px;font-weight:500;color:var(--ink)}
.promise-item{position:absolute;top:160px;width:220px;margin-left:-110px;text-align:center;font-size:14px;line-height:23px;color:var(--muted)}
.promise-item svg{display:block;margin:0 auto 22px}
.promise-item b{font-weight:600;color:var(--ink)}

/* checklist */
.checks{position:absolute;left:94px;top:2083px;width:460px}
.check{display:flex;gap:12px;margin-bottom:20px}
.check h4{font-size:22px;font-weight:500;color:var(--navy);line-height:28px}
.check p{font-size:13.5px;line-height:21px;color:var(--ink)}
.check svg{flex:none;margin-top:5px}
.cash-photo{left:634px;top:2033px;width:480px;height:351px;background:radial-gradient(circle at 38% 55%,#c8cbb8 0,#9ea08e 30%,#41506a 70%,#2a3a58 100%)}

/* contact */
.contact{position:absolute;left:0;top:2475px;width:1200px;height:528px;background:linear-gradient(100deg,#3b4048,#5c6670 40%,#7d8895 65%,#5a6470)}
.contact h2{position:absolute;left:85px;top:195px;font-size:31px;line-height:42px;font-weight:600;color:var(--white)}
.contact .script{position:absolute;left:85px;top:265px;font-family:"Yellowtail",cursive;font-size:52px;color:var(--green)}
.field{position:absolute;background:var(--white);font-size:12.5px;color:#9aa0a8;padding:12px 16px;border:1px solid #e0e0e0}

/* footer */
.site-footer{position:absolute;left:0;top:3003px;width:1200px;height:221px;background:var(--navy-deep);color:var(--white)}
.foot-brand{position:absolute;left:85px;top:78px;display:flex;align-items:center;gap:16px;font-size:21px}
.foot-brand .mark{width:50px;height:50px;border-radius:50%;background:var(--sky)}
.foot-brand b{font-weight:600}
.mail{position:absolute;left:813px;top:78px;width:44px;height:44px;border:1.5px solid var(--white);border-radius:50%;display:flex;align-items:center;justify-content:center}
.foot-call{position:absolute;left:870px;top:78px;width:244px;height:44px;border:1.5px solid var(--white);border-radius:22px;display:flex;align-items:center;justify-content:center;gap:6px;font-weight:600;font-size:16px}
.foot-call .dot{width:18px;height:18px;border-radius:50%;background:var(--green)}
.foot-rule{position:absolute;left:85px;top:150px;width:1029px;height:1px;background:rgba(255,255,255,.25)}
.copy{position:absolute;left:85px;top:177px;font-size:12px}
.foot-nav{position:absolute;right:86px;top:177px;display:flex;gap:30px;align-items:center;font-size:13px}
.foot-nav .sep{width:3px;height:3px;border-radius:50%;background:var(--white)}
</style>
</head>
<body>

<header class="site-header">
  <div class="call">Call. <span class="dot"><svg width="10" height="10" viewBox="0 0 10 10"><path d="M2 1.5l1.6 0 .6 2-1 .8a5 5 0 0 0 2.5 2.5l.8-1 2 .6v1.6c-3.6.3-6.8-2.9-6.5-6.5z" fill="#fff"/></svg></span> 555-014-2290</div>
  <div class="brand">BriskwayLane.com <span class="mark"></span></div>
  <div class="btn btn--green" style="left:863px;top:26px;width:176px;height:34px">Schedule Your Offer</div>
</header>

<nav class="main-nav">
  <span class="active">Sell Your Vehicle</span><span class="sep"></span>
  <span>How it Works</span><span class="sep"></span>
  <span>About</span><span class="sep"></span>
  <span>Contact</span>
</nav>

<section class="hero" role="img" aria-label="Smiling senior woman seated at the wheel of her car">
  <h1>Hassle-Free Way of<br>Sell your &nbsp;Car, RV, or Boat</h1>
  <p>in the Sun City Center, FL</p>
  <div class="btn btn--sky" style="left:85px;top:321px;width:177px;height:34px">Contact Us Today!</div>
</section>

<section class="chooser">
  <h2>Choose your vehicle to selling</h2>
  <div class="vehicle selected" style="left:204px">
    <div class="disc"><svg width="54" height="40" viewBox="0 0 54 40"><path d="M10 18l5-10c1-2 3-3 5-3h14c2 0 4 1 5 3l5 10h2c2 0 4 2 4 4v8H4v-8c0-2 2-4 4-4z" fill="#fff"/><rect x="16" y="9" width="22" height="9" rx="2" fill="#0f3a6d"/><circle cx="14" cy="31" r="6" fill="#0f3a6d" stroke="#fff" stroke-width="3"/><circle cx="40" cy="31" r="6" fill="#0f3a6d" stroke="#fff" stroke-width="3"/></svg></div>
    Car, SUV Truck
  </div>
  <div class="divider" style="left:338px"></div>
  <div class="vehicle" style="left:470px">
    <div class="disc"><svg width="48" height="36" viewBox="0 0 48 36"><rect x="4" y="6" width="40" height="22" rx="3" fill="#0f3a6d"/><rect x="9" y="10" width="8" height="6" fill="#fff"/><rect x="20" y="10" width="8" height="6" fill="#fff"/><rect x="31" y="10" width="8" height="6" fill="#fff"/><circle cx="13" cy="30" r="4" fill="#0f3a6d" stroke="#fff" stroke-width="2"/><circle cx="35" cy="30" r="4" fill="#0f3a6d" stroke="#fff" stroke-width="2"/></svg></div>
    RV's
  </div>
  <div class="divider" style="left:601px"></div>
  <div class="vehicle" style="left:728px">
    <div class="disc"><svg width="50" height="36" viewBox="0 0 50 36"><path d="M16 6h12v6h8v6H12z" fill="#0f3a6d"/><path d="M4 20h42l-6 10H10z" fill="#0f3a6d"/><path d="M4 33c4 0 4-2 8-2s4 2 8 2 4-2 8-2 4 2 8 2 4-2 8-2" stroke="#0f3a6d" stroke-width="2" fill="none"/></svg></div>
    Boat
  </div>
  <div class="divider" style="left:864px"></div>
  <div class="vehicle" style="left:995px">
    <div class="disc"><svg width="52" height="36" viewBox="0 0 52 36"><rect x="4" y="6" width="28" height="20" fill="#0f3a6d"/><path d="M34 12h8l6 7v7H34z" fill="#0f3a6d"/><circle cx="13" cy="28" r="4" fill="#0f3a6d" stroke="#fff" stroke-width="2"/><circle cx="40" cy="28" r="4" fill="#0f3a6d" stroke="#fff" stroke-width="2"/></svg></div>
    CV &amp; Fleet
  </div>
  <div class="btn btn--green" style="left:513px;top:309px;width:174px;height:34px">Schedule Your Offer</div>
</section>

<section class="about">
  <div class="abs about-photo" role="img" aria-label="Buyer and sellers talking beside a blue car in a showroom"></div>
  <div class="abs about-brand">BriskwayLane.com <span class="mark"></span></div>
  <div class="abs about-rule"></div>
  <h3>We offer the most convenient way of selling your vehicle.</h3>
  <p>We will come to you at a place of your choosing, i.e. home, office, or any other public place. &nbsp;We will give you an in person cash offer on the spot.</p>
  <div class="btn btn--sky" style="left:634px;top:1404px;width:124px;height:34px">About Us</div>
</section>

<section class="promise">
  <h2>Get your free in person cash offer today!<br>“Don’t Sell til you give me a yell”</h2>
  <div class="promise-item" style="left:204px">
    <svg width="70" height="70" viewBox="0 0 70 70" fill="none" stroke="#0f3a6d" stroke-width="3"><circle cx="35" cy="37" r="26"/><path d="M35 22v16l10 7"/><path d="M29 6h12"/></svg>
    <b>Fast</b> - I'll Be at Your<br>Door Today
  </div>
  <div class="promise-item" style="left:470px">
    <svg width="70" height="70" viewBox="0 0 70 70" fill="none" stroke="#0f3a6d" stroke-width="3"><circle cx="35" cy="35" r="32"/><circle cx="35" cy="35" r="25"/><path d="M42 26c-2-3-12-4-13 1-1 6 14 4 13 11-1 5-11 5-14 1M35 18v5M35 47v5"/></svg>
    <b>Fair</b> - Get Fair Price for<br>Your Vehicle
  </div>
  <div class="promise-item" style="left:728px">
    <svg width="70" height="70" viewBox="0 0 70 70" fill="none" stroke="#0f3a6d" stroke-width="3"><circle cx="35" cy="28" r="22"/><circle cx="35" cy="28" r="15"/><path d="M35 19l3 6 6 1-4 4 1 6-6-3-6 3 1-6-4-4 6-1z"/><path d="M22 46l-6 18 9-4 5 7 5-16M48 46l6 18-9-4-5 7-5-16"/></svg>
    <b>Friendly</b> - Trusted for Over<br>25 Years
  </div>
  <div class="promise-item" style="left:995px">
    <svg width="70" height="70" viewBox="0 0 70 70" fill="none" stroke="#0f3a6d" stroke-width="3"><circle cx="35" cy="35" r="32"/><path d="M22 36l9 9 17-19"/></svg>
    <b>Hassle Free</b> - I Handle All the<br>Paperwork
  </div>
</section>

<section>
  <div class="checks">
    <div class="check"><svg width="16" height="18" viewBox="0 0 16 18"><path d="M8 0l8 3v6c0 5-4 8-8 9-4-1-8-4-8-9V3z" fill="#a1cd3a"/><path d="M4 9l3 3 5-6" stroke="#fff" stroke-width="2" fill="none"/></svg>
      <div><h4>Got a nice car you just don’t need?</h4><p>I'll Buy It! – Stop wasting money on insurance, registration<br>and maintenance costs!</p></div></div>
    <div class="check"><svg width="16" height="18" viewBox="0 0 16 18"><path d="M8 0l8 3v6c0 5-4 8-8 9-4-1-8-4-8-9V3z" fill="#a1cd3a"/><path d="M4 9l3 3 5-6" stroke="#fff" stroke-width="2" fill="none"/></svg>
      <div><h4>Got an old clunker?</h4><p>I'll But It! – Turn it into cash today!</p></div></div>
    <div class="check"><svg width="16" height="18" viewBox="0 0 16 18"><path d="M8 0l8 3v6c0 5-4 8-8 9-4-1-8-4-8-9V3z" fill="#a1cd3a"/><path d="M4 9l3 3 5-6" stroke="#fff" stroke-width="2" fill="none"/></svg>
      <div><h4>Got a car that needs repairs?</h4><p>I'll Buy It! – No matter what the issue is I'll come take it<br>away today!</p></div></div>
  </div>
  <div class="abs cash-photo" role="img" aria-label="Hand holding a fan of hundred dollar bills"></div>
</section>

<section class="contact" role="img" aria-label="Buyer and seller shaking hands in a car lot">
  <h2>You are one step<br>closer to getting the</h2>
  <div class="script">Top Dollar</div>
  <svg class="abs" style="left:482px;top:134px" width="84" height="258" viewBox="0 0 84 258"><path d="M2 2C40 60 78 110 82 128 78 146 40 196 2 256" stroke="#fff" stroke-width="2" fill="none" opacity=".85"/></svg>
  <div class="field" style="left:634px;top:140px;width:233px;height:34px">Your Name</div>
  <div class="field" style="left:881px;top:140px;width:233px;height:34px">Contact No.</div>
  <div class="field" style="left:634px;top:188px;width:233px;height:34px">Email</div>
  <div class="field" style="left:881px;top:188px;width:233px;height:34px">Vehicle Type</div>
  <div class="field" style="left:634px;top:238px;width:152px;height:33px">Make</div>
  <div class="field" style="left:801px;top:238px;width:151px;height:33px">Model</div>
  <div class="field" style="left:963px;top:238px;width:151px;height:33px">Year</div>
  <div class="field" style="left:634px;top:285px;width:480px;height:104px">Type your Message ...</div>
  <div class="btn btn--green" style="left:787px;top:373px;width:175px;height:34px">Schedule Your Offer</div>
</section>

<footer class="site-footer">
  <div class="foot-brand"><span class="mark"></span><span><b>Briskway Lane.</b> &nbsp;Trusted Over 25 Years</span></div>
  <div class="mail"><svg width="16" height="12" viewBox="0 0 16 12"><rect x="1" y="1" width="14" height="10" rx="1" fill="#fff"/><path d="M1 2l7 5 7-5" stroke="#0c3363" stroke-width="1.5" fill="none"/></svg></div>
  <div class="foot-call">Call. <span class="dot"></span> 555-014-2290</div>
  <div class="foot-rule"></div>
  <div class="copy">© 2020 Briskway Lane. All right reserved.</div>
  <nav class="foot-nav"><span>Sell Your Vehicle</span><span class="sep"></span><span>How it Works</span><span class="sep"></span><span>About</span><span class="sep"></span><span>Contact</span></nav>
</footer>

</body>
</html>
```